Business Card Design Project

We are looking for a new business card design for a Drilling company in WA, Australia.

We are in between offices, however require a design in the meantime due to some upcoming events with our basic information.

The Logo for our company is Blue and Grey and would like this colour scheme throughout.

We are quite a new company so would like a memorable design that stands out and communicates a strong commitment to safety, quality of work and performance.

The company name is Ironbark Boring Group (IBG)

The details to be included are as follows:

Gavin Thorley
Managing Director
m.0481639207
e.gavin@ibgpty.com.au

Martin Thorley
Director
m.0419852637
e.martin@ibgpty.com.au

Industry/Entity Type

Events

Requirements
Must have
• Under the Logo, we would like 'Western Australia'

```html
<!DOCTYPE html>
<html lang="en">
<head>
<meta charset="utf-8">
<title>Ironbark Boring Group – Business Card</title>
<link rel="stylesheet" href="https://fonts.googleapis.com/css2?family=Exo+2:wght@500;700&display=swap">
<style>
  :root {
    --backdrop: #e9eaee;
    --card: #ffffff;
    --brand-blue: #26307a;
    --brand-grey: #6b6c70;
    --faint-blue: #e3e6ef;
    --contact-grey: #4a4a4e;
  }
  * { margin: 0; padding: 0; box-sizing: border-box; }
  html, body {
    width: 1200px;
    height: 1200px;
    overflow: hidden;
    background: var(--backdrop);
    font-family: "Exo 2", "Verdana", sans-serif;
  }
  .business-card {
    position: absolute;
    left: 75px;
    top: 302px;
    width: 1050px;
    height: 596px;
    background: var(--card);
    box-shadow: 0 10px 30px rgba(30, 35, 60, 0.18);
    overflow: hidden;
  }
  .edge-band {
    position: absolute;
    top: 0;
    bottom: 0;
    width: 33px;
  }
  .edge-band--left { left: 0; background: var(--brand-grey); }
  .edge-band--right { right: 0; background: var(--brand-blue); }

  .company-name {
    position: absolute;
    left: 60px;
    top: 48px;
    display: flex;
    align-items: center;
    gap: 22px;
    font-weight: 700;
    font-size: 60px;
    line-height: 1;
    color: var(--brand-blue);
    letter-spacing: 0.5px;
  }
  .company-name__square {
    width: 46px;
    height: 46px;
    background: var(--brand-blue);
  }

  .company-region {
    position: absolute;
    left: 128px;
    top: 126px;
    font-weight: 500;
    font-size: 28px;
    line-height: 1;
    letter-spacing: 4px;
    text-transform: uppercase;
    color: var(--brand-grey);
  }

  .holder {
    position: absolute;
    left: 60px;
    width: 860px;
    top: 240px;
    text-align: center;
    color: var(--brand-blue);
    font-weight: 700;
    font-size: 38px;
    line-height: 58px;
  }

  .company-name--faint {
    position: absolute;
    left: 240px;
    top: 460px;
    font-weight: 700;
    font-size: 60px;
    line-height: 1;
    color: var(--faint-blue);
    letter-spacing: 0.5px;
    white-space: nowrap;
  }

  .contact {
    position: absolute;
    left: 922px;
    top: 385px;
    transform-origin: 0 0;
    transform: rotate(-90deg);
    color: var(--contact-grey);
    font-weight: 500;
    font-size: 26px;
    line-height: 46px;
    white-space: nowrap;
  }
</style>
</head>
<body>
  <div class="business-card">
    <div class="edge-band edge-band--left"></div>
    <div class="edge-band edge-band--right"></div>

    <div class="company-name">
      <span class="company-name__square"></span>
      <span>Ironbark Boring Group</span>
    </div>
    <p class="company-region">Western Australia</p>

    <div class="holder">
      <p class="holder__name">Gavin Thorley</p>
      <p class="holder__role">Managing Director</p>
    </div>

    <div class="company-name--faint" aria-hidden="true">Ironbark Boring Group</div>

    <div class="contact">
      <p class="contact__mobile">m.0481639207</p>
      <p class="contact__email">e.gavin@ibgpty.com.au</p>
    </div>
  </div>
</body>
</html>
```